Laser Hair Removal Tri Fold brochure

I'm looking for a tri fold brochure (A4 size) for a cosmetic surgery centre / dermatology clinic for our laser hair removal services please.

Whilst we are more medical centre than spa, and cater to both men and women, some warmth would good to convey.

I've attached several versions of our logo - either can be used depending on the design style and colouring used. You can see more about us at www.qentrava.ae. I've also added some photos of our clinic if that is of any interest. No need to use them but they're there if you want them.

As we are based in the Middle East, no images showing too much skin should be used. Legs or face, or certain parts of the body are fine, so long as they aren't too revealing, as we need to be culturally sensitive.

One of our (non creative) staff has drafted a basic brochure using Word, which I've attached as a point of reference or for content, although naturally it's not professionally done so it's by no means a design guide! Also open to written content improvement if necessary but this part is non-essential. The only content I specifically want to keep is the price list please.

Many thanks!

Clinic

```html
<!DOCTYPE html>
<html lang="en">
<head>
<meta charset="utf-8">
<title>Qentrava – Laser Hair Removal Tri-Fold Brochure</title>
<link rel="stylesheet" href="https://fonts.googleapis.com/css2?family=Arimo:wght@400;700&family=Tinos:wght@400;700&family=Questrial&display=swap">
<style>
  :root{
    --rose:#c9436f;
    --rose-light:#e48aaa;
    --rose-pale:#f3c6d6;
    --berry:#9b1f4b;
    --berry-dark:#7c1239;
    --paper:#ffffff;
    --panel-grey:#ececec;
    --ink:#3a3a3a;
    --stage:#d9d9d9;
    --skin-a:#e9c3ad;
    --skin-b:#b98268;
  }
  *{box-sizing:border-box;margin:0;padding:0}
  html,body{width:1200px;height:900px;overflow:hidden}
  body{background:var(--stage);position:relative;font-family:"Arimo",Arial,sans-serif;color:var(--ink)}
  .sheet{position:absolute;width:580px;height:430px;overflow:hidden}
  .sheet--outside{left:30px;top:20px;background:var(--panel-grey)}
  .sheet--inside{left:590px;top:450px;background:var(--paper)}
  .bands{position:absolute;inset:0;width:580px;height:430px}

  /* Outside: price list panel */
  .price-panel{position:absolute;left:0;top:0;width:200px;height:430px;background:var(--rose);color:#fff;overflow:hidden}
  .price-panel__flower{position:absolute;right:-24px;top:-24px;width:64px;height:64px;border-radius:50%;background:var(--rose-light);opacity:.4}
  .price-panel__title{position:relative;padding-top:22px;text-align:center;font-weight:700;font-size:11.5px;line-height:1.25}
  .price-list{position:absolute;left:22px;right:24px;top:68px;list-style:none;font-size:7.9px}
  .price-list li{display:flex;justify-content:space-between;line-height:9.6px}

  /* Outside: cover panels */
  .brand-figure{position:absolute;left:250px;top:80px;width:80px;height:120px;background:linear-gradient(180deg,#e2e2e2,#d6d6d6);border-radius:40px 40px 10px 10px}
  .brand-name{position:absolute;left:200px;width:185px;top:208px;text-align:center;font-family:"Questrial",sans-serif;font-size:23px;letter-spacing:1px;color:#3d3d3d}
  .brand-sub{position:absolute;left:200px;width:185px;top:238px;text-align:center;font-size:5.5px;letter-spacing:2px;color:#555}
  .contact{position:absolute;left:200px;width:185px;top:322px;text-align:center;font-size:7px;line-height:9.3px;color:var(--rose);font-style:normal}
  .contact strong{font-weight:700}
  .brand-dot{position:absolute;left:287px;top:405px;width:11px;height:11px;border-radius:50%;background:var(--rose-light)}
  .cover-photo{position:absolute;left:385px;top:0;width:195px;height:300px;background:linear-gradient(135deg,#f4ede8 0%,var(--skin-a) 55%,var(--skin-b) 100%)}
  .cover-name{position:absolute;left:385px;width:195px;top:342px;text-align:center;font-family:"Questrial",sans-serif;font-size:22px;letter-spacing:1px;color:#3d3d3d}
  .cover-sub{position:absolute;left:385px;width:195px;top:368px;text-align:center;font-size:6.5px;letter-spacing:2px;color:#444}
  .partner-badge{position:absolute;left:462px;top:382px;width:40px;height:14px;background:#cfcfcf}

  /* Inside */
  .treatment-photo{position:absolute;left:0;top:0;width:580px;height:175px;background:linear-gradient(100deg,#d7b6a2 0%,var(--skin-a) 45%,#f1e6df 100%)}
  .col{position:absolute;top:172px;font-size:6.4px;line-height:8.3px;text-align:justify;color:var(--ink)}
  .col--left{left:20px;width:170px}
  .col--middle{left:206px;width:168px;top:168px}
  .col h2{font-family:"Tinos",serif;font-weight:700;color:var(--rose);font-size:13.5px;text-align:center;margin:6px 0 10px}
  .col p{margin-bottom:4px}
  .col .lead{color:var(--rose);font-weight:700}
  .col .lead-cap{color:var(--rose);font-weight:700;font-size:8.5px}
  .divider-dot{display:block;width:7px;height:7px;border-radius:50%;background:var(--rose-light);margin:6px auto 10px}

  .results{position:absolute;left:385px;top:150px;width:195px;height:280px}
  .result{position:absolute;width:50px;height:50px;border-radius:50%;border:2px solid var(--rose-pale)}
  .result--a{left:30px;top:20px;background:linear-gradient(135deg,#b48a74,#d6b29c)}
  .result--b{left:112px;top:20px;background:linear-gradient(135deg,#c79f88,#e2c4b1)}
  .result--c{left:30px;top:80px;background:linear-gradient(135deg,#e0b49c,#f2d8c8)}
  .result--d{left:112px;top:80px;background:linear-gradient(135deg,#e99e7a,#f6c6ad)}
  .tag{position:absolute;font-size:5px;font-weight:700;letter-spacing:.5px;color:#fff}
  .advantages{position:absolute;left:385px;top:290px;width:195px;color:#fff}
  .advantages h3{font-family:"Tinos",serif;font-weight:700;font-size:10px;text-align:center;margin-bottom:8px}
  .advantages ul{list-style:none;padding-left:22px;font-family:"Tinos",serif;font-size:6.6px}
  .advantages li{position:relative;padding-left:16px;line-height:13px}
  .advantages li::before{content:"";position:absolute;left:0;top:3px;width:6px;height:6px;background:var(--berry-dark)}
</style>
</head>
<body>

<section class="sheet sheet--outside" aria-label="Brochure outside">
  <div class="cover-photo" role="img" aria-label="Photo of a smiling woman with a red flower in her hair"></div>

  <svg class="bands" viewBox="0 0 580 430" aria-hidden="true">
    <path d="M200 300 Q390 262 580 282 L580 430 L200 430 Z" fill="#ececec"/>
    <path d="M200 288 Q390 244 580 262 L580 284 Q390 266 200 304 Z" fill="#c9436f"/>
    <path d="M200 280 Q390 238 580 254 L580 262 Q390 246 200 290 Z" fill="#e48aaa"/>
    <path d="M385 408 Q480 392 580 398 L580 430 L385 430 Z" fill="#c9436f"/>
    <path d="M385 402 Q480 386 580 392 L580 400 Q480 394 385 410 Z" fill="#e48aaa"/>
  </svg>

  <div class="price-panel">
    <div class="price-panel__flower" role="img" aria-label="Decorative flower"></div>
    <h1 class="price-panel__title">Laser Hair Removal<br>Price List</h1>
    <ul class="price-list">
      <li><span>Upper Lip</span><span>250</span></li>
      <li><span>Back of Hands</span><span>480</span></li>
      <li><span>Chin</span><span>300</span></li>
      <li><span>Chin and Neck</span><span>550</span></li>
      <li><span>Chin and Beard</span><span>500</span></li>
      <li><span>Beard Definition</span><span>640</span></li>
      <li><span>Neck&amp; Beard Definition</span><span>750</span></li>
      <li><span>Full Beard</span><span>800</span></li>
      <li><span>Lower Half Face</span><span>700</span></li>
      <li><span>Lower Half Face and Neck</span><span>800</span></li>
      <li><span>Full Face</span><span>850</span></li>
      <li><span>Neck (Women)</span><span>320</span></li>
      <li><span>Full Neck</span><span>680</span></li>
      <li><span>Full Face and Neck</span><span>1000</span></li>
      <li><span>Full Breast (Women)</span><span>300</span></li>
      <li><span>Chest (Men)</span><span>1600</span></li>
      <li><span>Buttocks</span><span>1040</span></li>
      <li><span>Lower Back</span><span>1500</span></li>
      <li><span>Upper Back</span><span>1500</span></li>
      <li><span>Full Back</span><span>2000</span></li>
      <li><span>Abdomen</span><span>1100</span></li>
      <li><span>Underarms</span><span>600</span></li>
      <li><span>Half Arms</span><span>880</span></li>
      <li><span>Full Arms</span><span>1440</span></li>
      <li><span>Half Legs</span><span>1800</span></li>
      <li><span>Thighs</span><span>2100</span></li>
      <li><span>Full Legs</span><span>2600</span></li>
      <li><span>Bikini</span><span>650</span></li>
      <li><span>Bikini + Underarm</span><span>1050</span></li>
      <li><span>Full Bikini</span><span>1200</span></li>
      <li><span>Full Bikini + Underarm</span><span>1600</span></li>
      <li><span>Full Body</span><span>6400</span></li>
    </ul>
    <svg class="bands" viewBox="0 0 200 430" style="width:200px" aria-hidden="true">
      <path d="M0 418 Q110 396 200 400 L200 430 L0 430 Z" fill="#e48aaa"/>
    </svg>
  </div>

  <div class="brand-figure" role="img" aria-label="Line drawing of a female figure"></div>
  <div class="brand-name">QENTRAVA</div>
  <div class="brand-sub">AESTHETICS CLINIC</div>

  <address class="contact">
    <strong>Qentrava Aesthetics Clinic</strong><br>
    Between 4th St (Rawda)<br>
    &amp; 10th St (Al Noor)<br>
    Opposite Palm Grove Park<br>
    PO BOX 100742<br>
    Abu Dhabi, UAE<br>
    T: +971 2 555 0148<br>
    E: info@qentrava.ae
  </address>
  <span class="brand-dot"></span>

  <div class="cover-name">QENTRAVA</div>
  <div class="cover-sub">LASER HAIR REMOVAL</div>
  <span class="partner-badge"></span>
</section>

<section class="sheet sheet--inside" aria-label="Brochure inside">
  <div class="treatment-photo" role="img" aria-label="Photo of a woman receiving laser treatment on her face"></div>

  <svg class="bands" viewBox="0 0 580 430" aria-hidden="true">
    <path d="M0 176 Q290 126 580 150 L580 430 L0 430 Z" fill="#ffffff"/>
    <path d="M0 164 Q290 112 580 136 L580 152 Q290 128 0 178 Z" fill="#c9436f"/>
    <path d="M0 158 Q290 106 580 128 L580 137 Q290 114 0 166 Z" fill="#e48aaa"/>
    <path d="M385 148 Q480 140 580 148 L580 430 L385 430 Z" fill="#9b1f4b"/>
    <path d="M0 426 Q290 400 580 410 L580 430 L0 430 Z" fill="#e48aaa"/>
    <path d="M0 430 Q290 408 580 418 L580 430 Z" fill="#c9436f"/>
  </svg>

  <div class="col col--left">
    <h2>Laser Hair Removal</h2>
    <p><span class="lead-cap">A</span><span class="lead">lmost our entire body</span> is covered with hair. Most of it is fine and pale, however we almost all have darker, coarse hair in places we wouldn't want or expect. It may be a question of aesthetics or hygiene; in any case, this excess body hair is often considered as embarrassing and bothersome, especially in places like legs, bikini line, neck, arms and armpits, chest and back.</p>
    <span class="divider-dot"></span>
    <p><span class="lead">Laser hair removal</span> is becoming more and more mainstream with women as well as men; it is one of the most popular aesthetic treatments in practices all over the world. No one really wants to have more discomfort, ingrown hair and irritated or infected skin, which is the usual consequence of shaving, plucking, waxing… and it has to be repeated over and over again. Laser hair removal is a long-lasting, comfortable solution!</p>
  </div>

  <div class="col col--middle">
    <p><span class="lead">Laser hair removal</span> is a much faster and more efficient procedure than most other available treatments. Laser light targets hair follicles and eliminates or significantly impedes hair from growing back. The deep penetration of Nd:YAG laser ensures it reaches even the deepest follicles, while its low absorption in all skin types ensures the surrounding tissue is preserved. This guarantees safe, fast and effective hair removal, even in the darkest skin types, without the epidermal damage other light-based treatments inherently cause. The procedure is quick and largely pain-free. You will be able to return to your normal activities immediately.</p>
    <span class="divider-dot"></span>
    <p><span class="lead">Because hair grows in cycles</span>, it takes several treatments for complete removal. The outcome also depends on hair quality and the quantity of hair follicles, along with the metabolism and hormonal level of each individual. As a guide, however, four to six treatments are usually all that are required to effectively remove all the hair.</p>
  </div>

  <div class="results">
    <span class="result result--a" role="img" aria-label="Skin before treatment"></span>
    <span class="result result--b" role="img" aria-label="Skin after treatment"></span>
    <span class="result result--c" role="img" aria-label="Skin before treatment"></span>
    <span class="result result--d" role="img" aria-label="Skin after treatment"></span>
    <span class="tag" style="left:6px;top:50px">BEFORE</span>
    <span class="tag" style="left:166px;top:28px">AFTER</span>
    <span class="tag" style="left:6px;top:112px">BEFORE</span>
    <span class="tag" style="left:166px;top:90px">AFTER</span>
  </div>

  <div class="advantages">
    <h3>Advantages of Laser Hair Removal</h3>
    <ul>
      <li>Safe and effective</li>
      <li>Fast and convenient</li>
      <li>Long lasting results</li>
      <li>Suitable for all skin types</li>
      <li>No pain, ingrown hair or infected skin</li>
      <li>Suitable for larger and smaller areas</li>
    </ul>
  </div>
</section>

</body>
</html>
```